Brightmoor Dental Care Stationery

create stationery, business cards and envelops for business. Use current logo on website but open to new fonts for the business name. Business name is Brightmoor Dental Care, would like below the name added "Cosmetic - Family - Implants" Website is www.brightmoordentalcareXQ.example. I would like to have modern look, clean, and professional. The water mark of the logo is a great thing to ad as well.

Target Market(s)

General public, Families, Cosmetic, Implant

Industry/Entity Type

Dental

Font styles to use
Sans Serif

Colors
9bcb3c
000000
757575
c9c9c9

Requirements
Must have
• Would like to see different versions of the current logo. Improvements, color, sytle, and class.
Nice to have
• current font has double "oo" in the Brightmoor logo, does not need to have with new logo.

```html
<!DOCTYPE html>
<html lang="en">
<head>
<meta charset="utf-8">
<title>Brightmoor Dental Care – Business Cards</title>
<link href="https://fonts.googleapis.com/css2?family=Montserrat:wght@500;600;700&display=swap" rel="stylesheet">
<style>
  :root {
    --bg: #ece9e6;
    --brown: #3b2922;
    --brown-light: #4f3a31;
    --red: #e3261f;
    --white: #ffffff;
    --ink: #2e211b;
    --watermark-dark: rgba(255,255,255,0.07);
    --watermark-light: rgba(0,0,0,0.05);
  }
  * { margin: 0; padding: 0; box-sizing: border-box; }
  html, body { width: 1200px; height: 1000px; overflow: hidden; }
  body {
    background: var(--bg);
    font-family: "Montserrat", Arial, sans-serif;
    position: relative;
  }
  .card {
    position: absolute;
    left: 250px;
    width: 700px;
    height: 400px;
    overflow: hidden;
    box-shadow: 0 8px 24px rgba(0,0,0,0.18);
  }
  .card-back {
    top: 60px;
    background: linear-gradient(120deg, var(--brown) 0%, var(--brown) 45%, var(--brown-light) 100%);
  }
  .card-front {
    top: 540px;
    background: var(--white);
  }
  .watermark {
    position: absolute;
    border-radius: 50%;
  }
  .card-back .watermark {
    right: 40px; top: 40px; width: 190px; height: 190px;
    border: 6px solid var(--watermark-dark);
  }
  .card-front .watermark {
    right: 20px; top: 60px; width: 200px; height: 200px;
    border: 6px solid var(--watermark-light);
  }
  .brand {
    position: absolute;
    display: flex;
    align-items: center;
    gap: 16px;
  }
  .brand-mark {
    width: 70px; height: 70px;
    border: 5px solid var(--red);
    border-radius: 50%;
    flex: none;
  }
  .brand-name {
    font-weight: 700;
    font-size: 30px;
    letter-spacing: 0.5px;
    line-height: 1;
    text-transform: uppercase;
  }
  .brand-tagline {
    margin-top: 6px;
    font-weight: 600;
    font-size: 12px;
    text-align: right;
  }
  .card-back .brand { left: 90px; top: 110px; }
  .card-back .brand-name { color: var(--white); font-size: 24px; }
  .card-back .brand-tagline { color: var(--white); }
  .website {
    position: absolute;
    left: 150px; top: 300px;
    color: var(--white);
    font-weight: 600;
    font-size: 20px;
    letter-spacing: 0.5px;
  }
  .card-front .brand { left: 150px; top: 55px; }
  .card-front .brand-name { color: var(--ink); font-size: 24px; }
  .card-front .brand-tagline { color: var(--ink); }
  .person {
    position: absolute;
    right: 340px; top: 225px;
    text-align: right;
    color: var(--ink);
    font-weight: 700;
    font-size: 19px;
    line-height: 1.2;
  }
  .divider {
    position: absolute;
    left: 378px; top: 190px;
    width: 3px; height: 100px;
    background: var(--red);
  }
  .contact {
    position: absolute;
    left: 398px; top: 188px;
    list-style: none;
    color: var(--ink);
    font-weight: 500;
    font-size: 19px;
    line-height: 1.25;
  }
  .band-brown {
    position: absolute;
    left: 0; right: 0; bottom: 0; height: 24px;
    background: var(--brown);
  }
  .band-brown-tab {
    position: absolute;
    right: 0; bottom: 0; width: 150px; height: 70px;
    background: var(--brown);
  }
  .band-red {
    position: absolute;
    left: 0; bottom: 24px; width: 550px; height: 30px;
    background: linear-gradient(90deg, var(--red), #ef3a2f);
  }
</style>
</head>
<body>
  <section class="card card-back" aria-label="Business card back">
    <div class="watermark" aria-hidden="true"></div>
    <div class="brand">
      <span class="brand-mark" aria-hidden="true"></span>
      <div>
        <p class="brand-name">Brightmoor Dental Care</p>
        <p class="brand-tagline">Cosmetic - Family - Implants</p>
      </div>
    </div>
    <p class="website">www.brightmoordentalcareXQ.example</p>
  </section>

  <section class="card card-front" aria-label="Business card front">
    <div class="watermark" aria-hidden="true"></div>
    <div class="brand">
      <span class="brand-mark" aria-hidden="true"></span>
      <div>
        <p class="brand-name">Brightmoor Dental Care</p>
        <p class="brand-tagline">Cosmetic - Family - Implants</p>
      </div>
    </div>
    <div class="person">
      <p class="person-name">Your Name</p>
      <p class="person-role">Position</p>
    </div>
    <div class="divider" aria-hidden="true"></div>
    <ul class="contact">
      <li>name@example.com</li>
      <li>000.000.0000</li>
      <li>000.000.0000</li>
    </ul>
    <div class="band-brown-tab" aria-hidden="true"></div>
    <div class="band-red" aria-hidden="true"></div>
    <div class="band-brown" aria-hidden="true"></div>
  </section>
</body>
</html>
```